Waste, Recycling & Food Waste Signage

We need 3 simple signs made to identify our waste, recycling and food waste bins. The signs should read
1. Food Scraps Only
2. Recycling Only
3. Trash
We'd like a simple logo to identify each. This simple logo or graphic will help our residents identify which bin to place their waste. We will be putting these signs in our parks and public spaces. The signs will either be affixed above the bin or on the bin. They need to be easily identifiable from a distance.
I've seen some use the following colors
1. Food Scraps Only (green sign)
2. Recycling Only (blue sign)
3. Trash (black sign)
Target Market(s)
Residents, general public
Requirements
Must have
- Need it to be simple and easy to see.

```html
<!DOCTYPE html>
<html lang="en">
<head>
<meta charset="utf-8">
<title>Bin Signs</title>
<link href="https://fonts.googleapis.com/css2?family=Barlow:wght@700&display=swap" rel="stylesheet">
<style>
  :root {
    --backdrop: #7b7b7b;
    --card: #ffffff;
    --trash: #231f20;
    --trash-tint: #d9d8d8;
    --recycling: #2a3a93;
    --recycling-tint: #cfd4ea;
    --food: #3cb54a;
    --food-tint: #cdebd0;
  }
  html, body { margin: 0; padding: 0; overflow: hidden; }
  body {
    width: 1200px; height: 817px;
    background: var(--backdrop);
    position: relative;
    font-family: "Barlow", "Arial Narrow", sans-serif;
  }
  .sign {
    position: absolute;
    background: var(--card);
    color: var(--accent);
  }
  .sign--trash { --accent: var(--trash); --tint: var(--trash-tint); left: 54px; top: 158px; width: 341px; height: 386px; }
  .sign--recycling { --accent: var(--recycling); --tint: var(--recycling-tint); left: 423px; top: 158px; width: 350px; height: 395px; }
  .sign--food { --accent: var(--food); --tint: var(--food-tint); left: 805px; top: 156px; width: 346px; height: 390px; }

  .sign__frame {
    position: absolute;
    left: 9px; right: 9px; top: 8px; bottom: 8px;
    border: 5px solid var(--accent);
    border-radius: 40px;
    overflow: hidden;
    box-sizing: border-box;
  }
  .sign__icon {
    position: absolute;
    left: 50%; top: 22px;
    width: 206px; height: 206px;
    transform: translateX(-50%);
  }
  .sign__ring { fill: var(--tint); stroke: var(--accent); stroke-width: 11; }
  .sign__title {
    position: absolute;
    left: 0; right: 0;
    bottom: 70px;
    margin: 0;
    text-align: center;
    font-weight: 700;
    font-size: 58px;
    line-height: 1;
    letter-spacing: 0.5px;
  }
  .sign--recycling .sign__title { font-size: 54px; bottom: 72px; }
  .sign--food .sign__title { font-size: 45px; bottom: 72px; }
  .sign__band {
    position: absolute;
    left: 0; right: 0; bottom: 0;
    height: 66px;
    background: var(--accent);
    color: var(--card);
    text-align: center;
    font-weight: 700;
    font-size: 42px;
    line-height: 62px;
  }
  .sign--recycling .sign__band { height: 68px; line-height: 64px; }
</style>
</head>
<body>

  <section class="sign sign--trash">
    <div class="sign__frame">
      <svg class="sign__icon" viewBox="0 0 200 200" role="img" aria-label="Trash can icon in a circle">
        <circle class="sign__ring" cx="100" cy="100" r="94"/>
      </svg>
      <h2 class="sign__title">TRASH</h2>
      <div class="sign__band">ONLY</div>
    </div>
  </section>

  <section class="sign sign--recycling">
    <div class="sign__frame">
      <svg class="sign__icon" viewBox="0 0 200 200" role="img" aria-label="Recycling arrows icon in a circle">
        <circle class="sign__ring" cx="100" cy="100" r="94"/>
      </svg>
      <h2 class="sign__title">RECYCLING</h2>
      <div class="sign__band">ONLY</div>
    </div>
  </section>

  <section class="sign sign--food">
    <div class="sign__frame">
      <svg class="sign__icon" viewBox="0 0 200 200" role="img" aria-label="Burger icon in a circle">
        <circle class="sign__ring" cx="100" cy="100" r="94"/>
      </svg>
      <h2 class="sign__title">FOOD SCRAPS</h2>
      <div class="sign__band">ONLY</div>
    </div>
  </section>

</body>
</html>
```